The Jawline Remedy Business Card

Looking for a business card design: front and back. It will be printed at presspanda.example on a leaf cutout trifecta paper with green middle. 3.5 x 2 leaf cutout. It will need bleed room around edges. The front will have my picture, logo, website and email address. The back will be a quote. "Finally. The complete solution to helping you open your mouth fully without pain"
and
"Like Us on Chatterbox to Learn More @ The Jawline Remedy"

Target Market(s)

Women 20-55 years old

Industry/Entity Type

Health Service

Contact Information for Business Card

My photo on one side or embedded, Name: Dr. Marlon Quaid, PT, DPT, MS Website: TheJawlineRemedy.example Email: marlon@keystonemotionclinic.example

Requirements
Must have
• Unique design consistent with my logo

```html
<!DOCTYPE html>
<html lang="en">
<head>
<meta charset="utf-8">
<title>The Jawline Remedy – Business Card</title>
<link href="https://fonts.googleapis.com/css2?family=Poppins:wght@400;500;600;700&display=swap" rel="stylesheet">
<style>
  :root {
    --blue: #1f6fb8;
    --blue-deep: #1a5ea6;
    --green: #8cc63f;
    --green-edge: #2f8a2c;
    --white: #ffffff;
    --page: #e9ecef;
    --teal: #4c9bb0;
    --shirt: #b9cfe8;
    --shirt-deep: #8fb0d6;
  }
  * { box-sizing: border-box; margin: 0; padding: 0; }
  html, body { width: 1200px; height: 900px; overflow: hidden; }
  body {
    background: var(--page);
    font-family: "Poppins", sans-serif;
    display: flex;
    flex-direction: column;
    align-items: center;
    justify-content: center;
    gap: 40px;
  }
  .card {
    position: relative;
    width: 630px;
    height: 360px;
    overflow: hidden;
    border-bottom: 4px solid var(--green-edge);
    box-shadow: 0 6px 18px rgba(0,0,0,.18);
  }
  /* Back side */
  .card-back { background: var(--blue); }
  .card-back .wave { position: absolute; inset: 0; width: 100%; height: 100%; }
  .quote {
    position: absolute;
    top: 92px; left: 60px; right: 60px;
    color: var(--white);
    font-weight: 600;
    font-size: 24px;
    line-height: 1.3;
    text-align: center;
  }
  .quote .mark { color: var(--green); font-size: 34px; line-height: 0; vertical-align: -8px; }
  .social-line {
    position: absolute;
    right: 40px; bottom: 40px;
    display: flex; align-items: center; gap: 10px;
    color: var(--white);
    font-size: 15px;
    white-space: nowrap;
  }
  .social-line .square { width: 22px; height: 22px; background: var(--white); }
  .social-line .network { font-weight: 600; font-size: 17px; }
  /* Front side */
  .card-front { background: var(--white); }
  .photo-frame {
    position: absolute; left: -40px; top: 20px;
    width: 340px; height: 340px; border-radius: 50%;
    background: linear-gradient(160deg, var(--green) 0%, var(--teal) 55%, var(--blue) 100%);
  }
  .portrait {
    position: absolute; inset: 16px; border-radius: 50%;
    background: linear-gradient(180deg, var(--shirt) 0%, var(--shirt-deep) 100%);
  }
  .brand {
    position: absolute; top: 48px; left: 335px;
    display: flex; align-items: center; gap: 14px;
  }
  .brand .circle {
    width: 74px; height: 74px; border-radius: 50%;
    border: 4px solid var(--blue);
  }
  .brand .name {
    color: var(--green);
    font-weight: 600;
    font-size: 30px;
    line-height: 1.05;
  }
  .contact {
    position: absolute; left: 300px; right: 26px; bottom: 40px;
    text-align: right;
  }
  .contact .person {
    color: var(--blue-deep); font-weight: 700; font-size: 18px; text-transform: uppercase;
    white-space: nowrap;
  }
  .contact .person .creds { color: var(--green); font-weight: 500; }
  .contact .line {
    display: flex; justify-content: flex-end; align-items: center; gap: 8px;
    color: var(--blue-deep); font-size: 13.5px; margin-top: 6px; white-space: nowrap;
  }
  .contact .line svg { width: 14px; height: 14px; flex: none; }
</style>
</head>
<body>

  <section class="card card-back" aria-label="Card back">
    <svg class="wave" viewBox="0 0 630 360" preserveAspectRatio="none" aria-hidden="true">
      <path d="M0 360 L0 330 C 80 230, 200 215, 330 225 C 470 235, 560 150, 630 110 L630 360 Z" fill="#8cc63f"/>
    </svg>
    <p class="quote"><span class="mark">“</span> Finally. The complete solution to helping you open your mouth fully without pain <span class="mark">”</span></p>
    <div class="social-line">
      <span class="square"></span>
      <span>Like us on <span class="network">Chatterbox</span> to Learn More @ The Jawline Remedy</span>
    </div>
  </section>

  <section class="card card-front" aria-label="Card front">
    <div class="photo-frame">
      <div class="portrait" role="img" aria-label="Portrait photo of Dr. Marlon Quaid in a light blue shirt and striped tie"></div>
    </div>
    <div class="brand">
      <span class="circle"></span>
      <span class="name">The<br>Jawline<br>Remedy</span>
    </div>
    <div class="contact">
      <p class="person">Dr. Marlon Quaid, <span class="creds">PT, DPT, MS</span></p>
      <p class="line">www.TheJawlineRemedy.example
        <svg viewBox="0 0 16 16" aria-hidden="true"><circle cx="8" cy="8" r="7" fill="none" stroke="#8cc63f" stroke-width="1.4"/><ellipse cx="8" cy="8" rx="3" ry="7" fill="none" stroke="#8cc63f" stroke-width="1.2"/><path d="M1 8h14M2.5 4.5h11M2.5 11.5h11" stroke="#8cc63f" stroke-width="1.1"/></svg>
      </p>
      <p class="line">marlon@keystonemotionclinic.example
        <svg viewBox="0 0 16 16" aria-hidden="true"><rect x="1" y="3" width="14" height="10" fill="#8cc63f"/><path d="M1 3l7 6 7-6" fill="none" stroke="#fff" stroke-width="1.3"/></svg>
      </p>
    </div>
  </section>

</body>
</html>
```